businesscard, flyer and membercard

--------------------------------------------------------------------------------------------------
design flyer :
- delivering format (jpg, pdf and original psd)
- there is a example how the flyers should look like
the text and logo should be the same as the exemple flyer, the creativity is yours.
- the design should have a back and front side.
File format : 15,0 cm x 21,2 cm
design membercard :
- there is example how the member-card should look like
the text and logo should be the same as the exemple membercard, the creativity is yours.
- the front side contains text and open space where for writing :
Naam ......
Dansstijlen ......
- the front side contains 12 circels horizontal at the line name at the end of the line "Salsa".
- the front side contains 12 circels horizontal at the line name at the end of the line "Bachata".
- the front side contains 12 circels horizontal at the line name at the end of the line "Kizomba".
- each horizontal line with circels contains a different kind of color/design.
- file format: 7,6 cm x 10,7 cm
Business card :
- there is example how the businesscard should look like
the text and logo should be the same as the exemple buisinesscard, the creativity is yours.
- the design should have a back a front side
File format : 8,7 cm x 5,7 cm

Target Market(s)

Dancing :Salsa, Bachata and Kizomba

Colors

Designer to choose colors to be used in the design.

Requirements
Must have
• same text as seen on the examples.
Nice to have
• see the examples as attachments
Should not have
• - REMOVE TEXT "KOV" from the design
• - REMOVE TEXT "Gratis Parkeren"

```html
<!DOCTYPE html>
<html lang="nl">
<head>
<meta charset="utf-8">
<title>Solara Dance Studio – flyers, visitekaartjes en lidkaarten</title>
<link rel="stylesheet" href="https://fonts.googleapis.com/css2?family=Open+Sans:wght@400;600;700;800&display=swap">
<style>
  :root{
    --ink:#ffffff;
    --soft:#e9e4ea;
    --red:#e3141c;
    --deep-red:#9e0b14;
    --orange:#ff7a3a;
    --navy:#16152e;
    --violet:#4a3470;
    --black:#050505;
    --grey:#2a2a2e;
    --silver:#d9d9dd;
  }
  *{box-sizing:border-box;margin:0;padding:0}
  html,body{width:1200px;height:1200px;overflow:hidden;background:#fff}
  body{font-family:"Open Sans",Arial,sans-serif;color:var(--ink);position:relative}
  .piece{position:absolute;overflow:hidden}
  .abs{position:absolute;white-space:nowrap}
  .photo{position:absolute}

  /* brand block */
  .brand{position:absolute;text-align:center;transform:translateX(-50%)}
  .brand-name{display:inline-flex;align-items:center;gap:.3em;font-weight:700;letter-spacing:.08em;color:var(--ink)}
  .brand-dot{width:.5em;height:.5em;border-radius:50%;background:var(--red)}
  .brand-sub{display:block;font-weight:700;color:var(--ink)}

  /* flyers */
  .flyer{width:444px;height:626px}
  .flyer-schedule{background:
      radial-gradient(ellipse 60% 30% at 50% 0%,#ffb35a 0%,#f2542c 35%,rgba(200,40,60,0) 75%),
      linear-gradient(180deg,#d8322e 0%,#b12a52 28%,#5c4a8e 50%,#7a3b6e 68%,#c4161e 88%,#a10e14 100%)}
  .flyer-trial{background:
      radial-gradient(ellipse 60% 30% at 50% 0%,#ffb35a 0%,#f2542c 35%,rgba(200,40,60,0) 75%),
      linear-gradient(180deg,#d8322e 0%,#8a2146 22%,#2a1e3e 45%,#1b1932 70%,#16152e 100%)}
  .headline{font-weight:800;color:var(--silver);text-shadow:0 2px 4px rgba(0,0,0,.4)}
  .day{font-weight:700;font-size:15px;color:var(--soft);line-height:18.5px}
  .slot{font-size:15px;line-height:18.5px}
  .contact{font-size:12px;line-height:16px}
  .badge{position:absolute;border-radius:50%;background:var(--black);outline:1.5px dashed #fff;outline-offset:4px;display:flex;align-items:center;justify-content:center;text-align:center;line-height:1.25}
  .venue{font-weight:800;font-size:13px;color:var(--soft)}
  .style-list{font-weight:800;font-size:48px;line-height:58px;color:var(--silver);text-shadow:0 2px 5px rgba(0,0,0,.5)}
  .perks{font-size:18px;line-height:24px;text-align:right}

  /* cards */
  .card{background:var(--black)}
  .card-line{font-size:14px;line-height:18px}
  .icon{display:inline-block;width:10px;height:10px;margin-right:4px;vertical-align:-1px}

  /* member cards */
  .member{width:350px;height:229px;background:linear-gradient(90deg,var(--black) 0%,#120f1c 45%,#2d2250 70%,#7a1a2a 100%)}
  .member .title{font-weight:800;font-size:24px;color:var(--silver)}
  .member .field{font-size:12px;line-height:16px}
  .member .dots-line{display:inline-block;width:86px;border-bottom:1px dotted #fff;margin-left:3px}
  .member .dance{font-weight:800;font-size:24px;color:var(--silver)}
  .stamps{position:absolute;left:17px;display:grid;grid-template-columns:repeat(6,32px);column-gap:9.6px;row-gap:13px}
  .stamp{width:32px;height:32px;border-radius:50%;display:flex;align-items:center;justify-content:center;font-weight:700;font-size:17px}
  .stamps-bachata .stamp{background:#fff;color:#111;outline:1px dashed #fff;outline-offset:2px}
  .stamps-salsa .stamp{background:var(--red);color:#fff;outline:1px dashed #fff;outline-offset:2px}
  .stamps-kizomba .stamp{background:var(--grey);color:#fff;outline:1px dashed #aaa;outline-offset:2px}
  .member .foot{position:absolute;left:0;right:0;top:210px;text-align:center;font-size:8px}
</style>
</head>
<body>

<!-- Flyer: lesrooster -->
<section class="piece flyer flyer-schedule" style="left:54px;top:35px">
  <div class="photo" role="img" aria-label="Foto van een danspaar in avondkleding in een dramatische dans-pose" style="left:130px;top:175px;width:300px;height:380px;background:radial-gradient(ellipse at 50% 45%,rgba(60,20,40,.75) 0%,rgba(110,30,50,.45) 50%,rgba(0,0,0,0) 75%)"></div>
  <div class="brand" style="left:222px;top:40px">
    <span class="brand-name" style="font-size:26px">SOLARA<span class="brand-dot"></span></span>
    <span class="brand-sub" style="font-size:11px;margin-top:14px">DANCE STUDIO</span>
  </div>
  <div class="abs headline" style="left:0;width:444px;text-align:center;top:116px;font-size:44px;line-height:56px">LES ROOSTER</div>
  <div class="badge" style="left:346px;top:180px;width:72px;height:72px;font-size:12px">Altijd<br>Eerste les<br>GRATIS</div>

  <div class="abs" style="left:27px;top:193px">
    <div class="day">DINSDAG</div>
    <div class="slot">19:00 Salsa 1</div><div class="slot">20:00 Salsa 3</div><div class="slot">21:00 Bachata 3</div>
  </div>
  <div class="abs" style="left:27px;top:287px">
    <div class="day">WOENSDAG</div>
    <div class="slot">19:00 Kizomba 2</div><div class="slot">20:00 Kizomba 1</div><div class="slot">21:00 Kizomba 3</div>
  </div>
  <div class="abs" style="left:27px;top:380px">
    <div class="day">DONDERDAG</div>
    <div class="slot">19:00 Salsa 1</div><div class="slot">20:00 Bachata 2</div><div class="slot">21:00 Bachata 1</div>
  </div>

  <div class="abs headline" style="left:0;width:444px;text-align:center;top:467px;font-size:34px;line-height:44px">SALSA-BACHATA &amp;<br>KIZOMBA</div>
  <div class="abs contact" style="left:19px;top:564px">Parklaan 24, 2514 AB Den Haag<br>Facebook: Solaradenhaag<br>Tel: 0612 480 337</div>
  <div class="abs venue" style="right:19px;top:596px">CLUB VERANDA</div>
</section>

<!-- Flyer: gratis proeflessen -->
<section class="piece flyer flyer-trial" style="left:531px;top:35px">
  <div class="photo" role="img" aria-label="Foto van een danspaar, de danseres in rode jurk achterover gebogen" style="left:40px;top:200px;width:380px;height:330px;background:radial-gradient(ellipse at 55% 55%,rgba(225,40,40,.7) 0%,rgba(150,30,40,.35) 45%,rgba(0,0,0,0) 75%)"></div>
  <div class="brand" style="left:222px;top:40px">
    <span class="brand-name" style="font-size:26px">SOLARA<span class="brand-dot"></span></span>
    <span class="brand-sub" style="font-size:11px;margin-top:14px">DANCE STUDIO</span>
  </div>
  <div class="abs headline" style="left:0;width:444px;text-align:center;top:130px;font-size:32px">GRATIS PROEFLESSEN</div>
  <div class="abs headline" style="left:0;width:444px;text-align:center;top:167px;font-size:24px;font-weight:700">26 T/M 28 Sept</div>
  <div class="abs style-list" style="left:21px;top:302px">SALSA<br>BACHATA<br>KIZOMBA</div>
  <div class="abs perks" style="right:18px;top:466px">Erste les Gratis<br>Studente Korting<br>Elk niveau<br>Alle leeftijden</div>
  <div class="abs contact" style="left:19px;top:564px">Parklaan 24, 2514 AB Den Haag<br>Facebook: Solaradenhaag<br>Tel: 0612 480 337</div>
</section>

<!-- Visitekaartje voorzijde -->
<section class="piece card" style="left:54px;top:681px;width:373px;height:245px">
  <div class="photo" role="img" aria-label="Foto van een danspaar, de danseres in rode jurk met lichtvonken" style="left:170px;top:0;width:203px;height:245px;background:radial-gradient(ellipse at 55% 55%,#d8302a 0%,#7a1c1c 40%,#2a0f10 70%,var(--black) 100%)"></div>
  <div class="brand" style="left:123px;top:50px">
    <span class="brand-name" style="font-size:34px">SOLARA<span class="brand-dot"></span></span>
  </div>
  <div class="abs" style="left:0;width:246px;text-align:center;top:135px;font-weight:700;font-size:17px;line-height:21px">
    DANCE STUDIO<br><span style="font-size:18px;line-height:22px">SALSA<br>BACHATA<br>KIZOMBA</span>
  </div>
</section>

<!-- Visitekaartje achterzijde -->
<section class="piece card" style="left:54px;top:934px;width:372px;height:243px">
  <div class="photo" role="img" aria-label="Foto van een danspaar, de danseres in rode jurk met lichtvonken" style="left:150px;top:0;width:222px;height:243px;background:radial-gradient(ellipse at 55% 55%,#d8302a 0%,#7a1c1c 40%,#2a0f10 70%,var(--black) 100%)"></div>
  <div class="brand" style="left:74px;top:24px">
    <span class="brand-name" style="font-size:22px">SOLARA<span class="brand-dot"></span></span>
    <span class="brand-sub" style="font-size:10px;margin-top:18px">DANCE STUDIO</span>
  </div>
  <div class="abs" style="left:22px;top:118px">
    <div style="font-weight:700;font-size:14px;line-height:18px;padding-left:10px">Marisol</div>
    <div class="card-line"><svg class="icon" viewBox="0 0 10 10"><path d="M2 1l2 2-1 1.3c.6 1.2 1.5 2.1 2.7 2.7L7 6l2 2-1.4 1.5C4.5 9.2.8 5.5.5 2.4z" fill="var(--red)"/></svg>0612 480 337</div>
    <div class="card-line" style="margin-top:18px"><svg class="icon" viewBox="0 0 10 10"><rect x="0" y="2" width="10" height="6.5" fill="var(--red)"/><path d="M0 2l5 3.5L10 2" stroke="#000" stroke-width=".8" fill="none"/></svg>solaradans@mailpost.nl</div>
    <div class="card-line"><span class="icon" style="background:var(--red);border-radius:2px"></span>Solaradenhaag</div>
  </div>
</section>

<!-- Contactkaart -->
<section class="piece card" style="left:483px;top:681px;width:349px;height:228px;background:linear-gradient(90deg,var(--black) 0%,#0e0c16 45%,#2d2a5c 75%,#6a1524 100%)">
  <div class="photo" role="img" aria-label="Foto van een danspaar in avondkleding in een dramatische dans-pose" style="left:170px;top:0;width:179px;height:228px;background:radial-gradient(ellipse at 50% 50%,rgba(40,20,50,.85) 0%,rgba(70,30,70,.4) 50%,rgba(0,0,0,0) 80%)"></div>
  <div class="brand" style="left:69px;top:22px">
    <span class="brand-name" style="font-size:22px">SOLARA<span class="brand-dot"></span></span>
    <span class="brand-sub" style="font-size:10px;margin-top:18px">DANCE STUDIO</span>
  </div>
  <div class="abs" style="left:18px;top:110px">
    <div style="font-weight:700;font-size:14px;line-height:18px;padding-left:12px">Marisol</div>
    <div class="card-line"><svg class="icon" viewBox="0 0 10 10"><path d="M2 1l2 2-1 1.3c.6 1.2 1.5 2.1 2.7 2.7L7 6l2 2-1.4 1.5C4.5 9.2.8 5.5.5 2.4z" fill="var(--red)"/></svg>0612 480 337</div>
    <div class="card-line" style="margin-top:15px"><svg class="icon" viewBox="0 0 10 10"><rect x="0" y="2" width="10" height="6.5" fill="var(--red)"/><path d="M0 2l5 3.5L10 2" stroke="#000" stroke-width=".8" fill="none"/></svg>solaradans@mailpost.nl</div>
    <div class="card-line"><span class="icon" style="background:var(--red);border-radius:2px"></span>Solaradenhaag</div>
  </div>
</section>

<!-- Lidkaart Bachata -->
<section class="piece member" style="left:841px;top:681px">
  <div class="photo" role="img" aria-label="Foto van een danspaar in avondkleding" style="left:190px;top:0;width:160px;height:229px;background:radial-gradient(ellipse at 50% 50%,rgba(40,20,50,.8) 0%,rgba(0,0,0,0) 75%)"></div>
  <div class="brand" style="left:51px;top:14px"><span class="brand-name" style="font-size:13px">SOLARA<span class="brand-dot"></span></span><span class="brand-sub" style="font-size:6px;margin-top:9px">DANCE STUDIO</span></div>
  <div class="abs title" style="left:94px;top:8px">LID KAART</div>
  <div class="abs field" style="left:16px;top:61px">NAAM<span class="dots-line"></span><br>Dansstijlen<span class="dots-line" style="width:58px"></span></div>
  <div class="abs dance" style="left:16px;top:92px">BACHATA</div>
  <div class="stamps stamps-bachata" style="top:122px">
    <div class="stamp">1</div><div class="stamp">2</div><div class="stamp">3</div><div class="stamp">4</div><div class="stamp">5</div><div class="stamp">6</div>
    <div class="stamp">7</div><div class="stamp">8</div><div class="stamp">9</div><div class="stamp">10</div><div class="stamp">11</div><div class="stamp">12</div>
  </div>
  <div class="foot">Parklaan 24, 2514 AB Den Haag | Facebook: Solaradenhaag | Tel: 0612 480 337</div>
</section>

<!-- Lidkaart Salsa -->
<section class="piece member" style="left:483px;top:930px">
  <div class="photo" role="img" aria-label="Foto van een danspaar in avondkleding" style="left:190px;top:0;width:160px;height:229px;background:radial-gradient(ellipse at 50% 50%,rgba(40,20,50,.8) 0%,rgba(0,0,0,0) 75%)"></div>
  <div class="brand" style="left:51px;top:14px"><span class="brand-name" style="font-size:13px">SOLARA<span class="brand-dot"></span></span><span class="brand-sub" style="font-size:6px;margin-top:9px">DANCE STUDIO</span></div>
  <div class="abs title" style="left:94px;top:8px">LID KAART</div>
  <div class="abs field" style="left:16px;top:61px">NAAM<span class="dots-line"></span><br>Dansstijlen<span class="dots-line" style="width:58px"></span></div>
  <div class="abs dance" style="left:16px;top:92px">SALSA</div>
  <div class="stamps stamps-salsa" style="top:122px">
    <div class="stamp">1</div><div class="stamp">2</div><div class="stamp">3</div><div class="stamp">4</div><div class="stamp">5</div><div class="stamp">6</div>
    <div class="stamp">7</div><div class="stamp">8</div><div class="stamp">9</div><div class="stamp">10</div><div class="stamp">11</div><div class="stamp">12</div>
  </div>
  <div class="foot">Parklaan 24, 2514 AB Den Haag | Facebook: Solaradenhaag | Tel: 0612 480 337</div>
</section>

<!-- Lidkaart Kizomba -->
<section class="piece member" style="left:841px;top:930px">
  <div class="photo" role="img" aria-label="Foto van een danspaar in avondkleding" style="left:190px;top:0;width:160px;height:229px;background:radial-gradient(ellipse at 50% 50%,rgba(40,20,50,.8) 0%,rgba(0,0,0,0) 75%)"></div>
  <div class="brand" style="left:51px;top:14px"><span class="brand-name" style="font-size:13px">SOLARA<span class="brand-dot"></span></span><span class="brand-sub" style="font-size:6px;margin-top:9px">DANCE STUDIO</span></div>
  <div class="abs title" style="left:94px;top:8px">LID KAART</div>
  <div class="abs field" style="left:16px;top:61px">NAAM<span class="dots-line"></span><br>Dansstijlen<span class="dots-line" style="width:58px"></span></div>
  <div class="abs dance" style="left:16px;top:92px">KIZOMBA</div>
  <div class="stamps stamps-kizomba" style="top:122px">
    <div class="stamp">1</div><div class="stamp">2</div><div class="stamp">3</div><div class="stamp">4</div><div class="stamp">5</div><div class="stamp">6</div>
    <div class="stamp">7</div><div class="stamp">8</div><div class="stamp">9</div><div class="stamp">10</div><div class="stamp">11</div><div class="stamp">12</div>
  </div>
  <div class="foot">Parklaan 24, 2514 AB Den Haag | Facebook: Solaradenhaag | Tel: 0612 480 337</div>
</section>

</body>
</html>
```